Gift Card Design - Suds Harbor Lane

I am needing a design for a standard plastic gift card, (ever so slightly large then a standard rounded edge business card). Name of the business is Suds Harbor Lane. Attached is a file with a poor example, done by an equipment manufacturing firm, that I feel could be much better. Simple, clean and classy with what it is and does along with our name is what I am looking for. Attached also is out logo and source of logo, they don't have to be on the card.

Target Market(s)

Car wash customers in an upscale market.

Industry/Entity Type

Business

Font styles to use
Serif
Other font styles liked:
• whatever you feel, but I do like the font on a Verlance golf ball

Requirements
Must have
• Words anywhere on the card -
• Reloadable Card
• Self Serve Bays & Vacuums.
• Also need name of the business, Suds Harbor Lane.
Nice to have
• Work in Pantone #7483 as there is existing signage with that as a primary color, just trying to tie things together. Attached is my business logo and a picture of the source of the logo, you do not have to use those if you don't want to. I do like clean and classy but am open to creativity, that's why I am submitting this project.
Should not have
• Naked lady pictures

```html
<!DOCTYPE html>
<html lang="en">
<head>
<meta charset="utf-8">
<title>Suds Harbor Lane – Reloadable Card</title>
<link rel="stylesheet" href="https://fonts.googleapis.com/css2?family=Source+Sans+3:wght@400;600;700&display=swap">
<style>
  :root {
    --green-deep: #0b5f32;
    --green: #0f8a47;
    --brown: #7a4a1e;
    --brown-dark: #3b2412;
    --brown-light: #b48a5e;
    --card-white: #ffffff;
    --backdrop: #ecebe7;
  }
  html, body {
    margin: 0;
    width: 1200px;
    height: 800px;
    overflow: hidden;
    background: var(--backdrop);
    font-family: "Source Sans 3", "Myriad Pro", sans-serif;
  }
  .stage {
    width: 1200px;
    height: 800px;
    display: flex;
    align-items: center;
    justify-content: center;
  }
  .gift-card {
    width: 1000px;
    height: 600px;
    border-radius: 28px;
    box-shadow: 0 10px 30px rgba(0,0,0,0.18);
    overflow: hidden;
    background: var(--card-white);
  }
  .gift-card svg { display: block; }
  .card-heading { font-size: 58px; font-weight: 600; fill: var(--card-white); letter-spacing: 3px; }
  .card-title { font-size: 44px; font-weight: 700; fill: var(--brown-dark); letter-spacing: 1px; }
  .card-subtitle { font-size: 30px; font-weight: 400; fill: var(--brown); }
  .brand-name { font-size: 30px; font-weight: 600; fill: var(--brown); }
  .contact-text { font-size: 15px; font-weight: 400; fill: var(--card-white); }
  .contact-icon { fill: var(--card-white); }
</style>
</head>
<body>
<main class="stage">
  <section class="gift-card" aria-label="Suds Harbor Lane reloadable gift card">
    <svg width="1000" height="600" viewBox="0 0 1000 600" xmlns="http://www.w3.org/2000/svg">
      <defs>
        <linearGradient id="band-green" x1="0" y1="0" x2="1" y2="1">
          <stop offset="0" stop-color="var(--green-deep)"/>
          <stop offset="0.5" stop-color="var(--green)"/>
          <stop offset="1" stop-color="var(--green-deep)"/>
        </linearGradient>
        <linearGradient id="stripe-top" x1="1" y1="0" x2="0" y2="0">
          <stop offset="0" stop-color="var(--brown)"/>
          <stop offset="1" stop-color="var(--brown-light)" stop-opacity="0"/>
        </linearGradient>
        <linearGradient id="stripe-bottom" x1="0" y1="0" x2="1" y2="0">
          <stop offset="0" stop-color="var(--brown)"/>
          <stop offset="1" stop-color="var(--brown-light)" stop-opacity="0.2"/>
        </linearGradient>
      </defs>

      <!-- top band -->
      <path class="stripe-top" d="M1000,282 C780,222 480,102 0,40 L0,48 C480,120 780,248 1000,308 Z" fill="url(#stripe-top)"/>
      <path class="band-top" d="M0,0 H1000 V282 C780,222 480,102 0,40 Z" fill="url(#band-green)"/>
      <text class="card-heading" x="410" y="150" transform="rotate(9 680 130)">SUDS HARBOR LANE</text>

      <!-- bottom band -->
      <path class="stripe-bottom" d="M0,300 C320,322 700,450 1000,540 L1000,552 C700,464 320,340 0,322 Z" fill="url(#stripe-bottom)"/>
      <path class="band-bottom" d="M0,334 C320,354 700,474 1000,562 V600 H0 Z" fill="url(#band-green)"/>

      <!-- brand -->
      <g class="brand" transform="rotate(9 200 200)">
        <circle cx="110" cy="190" r="22" fill="var(--green)"/>
        <text class="brand-name" x="145" y="180">Suds Harbor</text>
        <text class="brand-name" x="145" y="214">Lane</text>
      </g>

      <!-- title -->
      <g class="card-message" transform="rotate(11 500 300)">
        <text class="card-title" x="360" y="280">RELOADABLE CARD</text>
        <text class="card-subtitle" x="340" y="316">Self Serve Bays &amp; Vacuums</text>
      </g>

      <!-- contact -->
      <g class="contact" transform="rotate(12 40 380)">
        <circle class="contact-icon" cx="46" cy="384" r="5"/>
        <text class="contact-text" x="58" y="389">www.sudsharborlane.com</text>
      </g>
      <g class="contact" transform="rotate(16 330 440)">
        <path class="contact-icon" d="M336,432 a5,5 0 1,1 0.1,0 Z M336,444 l-4,-8 h8 Z"/>
        <text class="contact-text" x="346" y="442">418 Marlow Ridge Road Eastbrook, TX 77390</text>
      </g>
      <g class="contact" transform="rotate(16 760 540)">
        <path class="contact-icon" d="M756,532 q-2,6 4,12 q6,6 12,4 l-2,-4 q-3,1 -6,-2 q-3,-3 -2,-6 Z"/>
        <text class="contact-text" x="778" y="545">555.014.2736</text>
      </g>
    </svg>
  </section>
</main>
</body>
</html>
```